International trading company needs banner designs for university careers fairs. Additional work to

Description
Our company, Meridale Capital, operates in the finance industry. We trade numerous financial instruments across the globe. We focus on futures, options, etfs and are currently expanding into the exciting area of cryptocurrencies. A main focus of ours is to use a systematic and quantitative approach to trading to develop and refine trading strategies that are relatively low risk in nature, but are scalable and provide positive returns. We work hard, we push each other to achieve great results. But at the same time we really enjoy each other’s company and share a relaxed atmosphere at work. Our website is http://www.meridalecapital.com.au/. Meridale will be attending university careers fairs and expos in coming months to attract the very best talent there is for graduate trading roles as well as graduate developer roles. As such, we require our booth to look professional. We want to convey our message that a career with us is exciting, rewarding, but also challenging. We aim to nurture talent and hope to provide the tools necessary to strive in a career in trading.

We have 3 aspects to our booth concept. But for this designer contest, we will focus on 1 of those projects. When we decide on one designer, we hope they will be willing to work one on one on the other 2 projects. On top of this contest, we are willing to pay $250 for the additional 2 projects, one of which is quite simple in design brief, the other will allow the designer the flare to be creative. It is important to note that all three concepts need to be cohesive. Each concept should complement the other in colour as well as message.

For the entire project to be finished, we are a little rushed on time and would require completion of all three concepts by February 2nd.

We will only require soft copy files so we can manage the print ourselves. We can accept a vector, eps or ai file.

For this contest project, the design concept is a pull-up banner. We will have 3 pull-up banners each with slightly different messages.

We have attached pictures to help inspire the designer. Also, we have attached company logo (a unicorn) and name, along with varying colour vectors.

Meridale Capital’s primary colours are black, green and white. We would like all 3 banners to be in the same scheme. But we are happy to see slightly different variations in design options on the colour scheme. We do feel that green writing on black background would look the sharpest and have the most impact. We could be wrong though and are fine to see different designs.

The banner dimensions will be 85cm wide x 210cm tall. So there is room on the banner to deliver an exciting, yet professional message.

Preliminary Pull-up Banner ideas
We are not designers, we are open to you, the designer, using your creative flare to design 3 sharp looking banners. We do have a rough idea of the direction of each banner though.

Banner 1 – A company inspired banner. We would like our company name, our logo (prominent!) and beneath it 3 to 4 words that describe what we’re about. For example, Challenging, Rewarding, Passionate, Entrepreneurial, Focused, Collaborative, Innovative, Systematic, Strategic. Happy for the designer to take control here.

For the rest of the banner we are open to design. Potentially a picture taken from our website that is reflective of our culture – which is relaxed, hard-working, collaborative, rewarding.

It doesn’t need to be too busy or cluttered, so no need to throw in designs that aren’t really consistent with us.

Banner 2 – A trader inspired banner. This is more designed to attract graduates interested in a career in trading. Include meridale name and logo. Maybe include a question for the students... Something like,
“Want to be challenged?
Want to strategise?
Want to be rewarded?
Become a trader!”
Doesn’t have to be straight angles, can be on an angle – designer free reign here. Also we can have different sentences, words. Up to the designer. We would like to include something that would attract a trader’s mind, something visual, like a trading chart. See attached pictures for trading chart examples.

Somewhere on the banner we can mention Graduate Trader Program, please contact us at careers@meridalecapital.com.au. Phone number below it (02) 7156 4830.

Banner 3 - A developer inspired banner. This is more designed to attract graduates interested in a career in developing. Include meridale name and logo

Put the following pitch on the banner and fill the rest of the space with designs and pictures. No fixed layout required here.

Good at problem solving? Obsessed with creating quality software? Love working with numbers? Do you speak programming language? Want to face fresh challenges each day?

On the banner we can mention Graduate Software Engineer Program, please contact us at careers@meridalecapital.com.au. Phone number below it (02) 7156 4830.

Additionally to the above 3 banners, we had an idea of including random words across the banners in random sizes and boldness. We’re not sure how this would appear so we would like to see a couple designs on this. We thought we could have a top tier of buzz words that should be more prominent with the second tier buzzwords in smaller size. Two design types - randomly displayed, secondly a bit more structured. Can decide what looks best when we receive design. Words below. We don’t have to include all of these words, whatever a good design lends itself to. Words should only be in green, black or white - consistent with our company scheme.

Top Tier Buzzwords
Trading
Cryptocurrency
Options
Market making
Trading
Bitcoin
Derivatives
ETF
Futures
Volatility
Arbitrage
Technology
HFT
Hedging

Second Tier Buzzwords
R&K 400
QMB 300
VLZ
DWT
QMB
FX
Bid
Offer
Margining
Long
Short
Spot
Position
Tolvar
Brimo
Wel Daro
WDI
GGI
Buy
Sell
Delta
Gamma
Vega
Theta
Skew
Straddle
Call

Once we have selected the designer, we are keen that they would complete another 2 projects for us. The other 2 projects are as follows:
• A double sided A5 flyer design – This should provide more information about what Meridale can offer the students as a career and a workplace. We will also give a small amount of detail about the graduate program.
• Table Cloth design – At each exhibition we receive a table at our booth. We would like to have a logo laden table cloth that will look professional

We would like the design scheme to flow neatly from the banners to the flyers to the table cloth. So the colours are consistent and our general tone/message is also consistent.

We have attached pictures that should help the designer. Included pictures of pull-up banners, pictures of student careers fairs, flyers, table cloth dimensions, Meridale’s logos and colour vectors.

Preliminary Double sided A5 Flyer ideas.

We would need two designs – a trader design and a developer design.

Art file to be supplied PDF file with trim marks & 3mm bleed

With the flyer we would like to add a little more information about Meridale on the front page (which should be the same for the trader flyer and the developer flyer). On the back page we would be a little more detailed in the graduate program. Give dates, the onboarding process, rough program details/info.

Front Page – Include Meridale name, logo. Explanation of who we are - proprietary trading firm, using our own capital to trade financial instruments around the world. We trade futures, options, etfs and cryptocurrencies (can make more elaborate).

To make it sound interesting we’d like to explain potential for growth in certain markets. So something along the lines, of “We are seeing rapid expansion in certain markets. At meridale we are always looking for new strategies and talent to expand our already growing presence. Working with Meridale, you’ll get exposure and experience on all of these exciting markets which will greatly benefit you in your career progression” (Doesn’t need to be word for word)

We’d also like to mention some of the perks of working with us:
daily lunch provided
cafe coffee
 breakfast/snacks
 casual attire
 cash bonus half yearly
 competitive rates
 team dinners
 gym membership
 company trips
We’d like to use consistent colour schemes with our company, Black and Green. Some white could work in there. But not a necessity.
The designer can feel free to add in some sharp looking images.

Back Page Trader Flyer - We would like to give some more info on the positives of the trader program. We’re mainly focusing on the strengths of the program here – listed below.
• 1 on 1 training
• In-depth theory classes with practical applications
• Experienced traders providing the training
• Live trading within 3 months
• Ongoing mentoring
• Exposure to different markets/strategies
• Placed onto products that best suit their strengths
• Simulated trader training based on actual events

We should also add contact details for students to apply to.
For more information on the Graduate Trader Program
contact us at careers@meridalecapital.com.au.
Phone number (02) 7156 4830.

OR

To apply please send through your CV and academic transcript to careers@meridalecapital.com.au

We would also want this to look quite sharp, so adding in a trading graph could make it look exciting and attractive.

Back Page Developer Flyer
• 1 on 1 mentoring by senior software engineers
• Full SDLC exposure
• Extremely agile environment
• Direct interaction with business and stakeholders
• Multiple career paths for future growth

For more information on the Graduate Software Engineer Program
Contact us at careers@meridalecapital.com.au.

OR

Preliminary table cloth ideas.
We would need two designs before choosing one.

First design is a very simple design that would look professional. A plain black design with MERIDALE on the front in Green.

The second design is plain black, MERIDALE on the front in Green, similar to above. But we’d also like to see the words mentioned above in the top tier and second tier randomly across the table cloth. In different sizes and weightings.
We’ll see which design looks the best and choose one.

References to see the products we’d be using:
https://brontelsigns.com.au/products/pull-up-banners
https://www.quorvelprint.com.au/lpt/flyers-sizes.aspx?mk=flyers+design&rd=1
https://www.tallowbanners.com.au/outdoor/custom-table-throws/loose-printed-table-throws.html

Target Market(s)

University Graduates in IT, Engineering, Maths, Sciences, Business that would be interested in a career of trading financial instruments including cryptocurrency, options, futures, ETFs. We are also targeting developers in the same space.

Industry/Entity Type

Finance

Font styles to use
Serif
Sans Serif

Colors
00a990
ffffff
000000
33b8a4
1b1b1b

Requirements
Must have
• Cohesion between banners and other project work.
• Clear message coming through
• Professional look
• Eye catching
• Attractive
• Colour schemes must work
Should not have
• Must not be boring. We are looking to project our company image. We are not boring so we want to see some creative flare. But we are also a professional firm so our designs must be sharp.

```html
<!DOCTYPE html>
<html lang="en">
<head>
<meta charset="utf-8">
<title>Meridale Capital – Careers Fair Pull-up Banners</title>
<link rel="stylesheet" href="https://fonts.googleapis.com/css2?family=Bebas+Neue&family=Lato:wght@300;400;700&family=Libre+Baskerville&display=swap">
<style>
  :root {
    --green: #00a990;
    --green-light: #33b8a4;
    --black: #000000;
    --charcoal: #1b1b1b;
    --white: #ffffff;
    --backdrop: #eeeeee;
    --font-display: "Bebas Neue", "Oswald", sans-serif;
    --font-body: "Lato", "Helvetica Neue", Arial, sans-serif;
    --font-serif: "Libre Baskerville", Georgia, serif;
  }
  * { box-sizing: border-box; margin: 0; padding: 0; }
  html, body { width: 1200px; height: 859px; overflow: hidden; }
  body { background: var(--backdrop); font-family: var(--font-body); }

  .canvas { position: relative; width: 1200px; height: 859px; }

  .banner {
    position: absolute; top: 60px;
    width: 300px; height: 740px;
    background: var(--black);
    overflow: hidden;
    box-shadow: 0 6px 18px rgba(0,0,0,.18);
  }
  .banner--company { left: 90px; }
  .banner--trader { left: 450px; }
  .banner--challenge { left: 810px; }

  .banner__shapes { position: absolute; inset: 0; width: 300px; height: 740px; }
  .layer { position: absolute; left: 0; width: 300px; text-align: center; }

  /* Wordmark */
  .wordmark { display: flex; align-items: center; justify-content: center; gap: 10px; }
  .wordmark__dot { width: 22px; height: 22px; border-radius: 50%; background: var(--green); }
  .wordmark__name {
    font-family: var(--font-body); font-weight: 300;
    color: var(--green); letter-spacing: 1px;
  }

  /* Banner 1 */
  .company-mark { top: 300px; display: flex; justify-content: center; }
  .company-mark__circle { width: 70px; height: 70px; border-radius: 50%; background: var(--green); }
  .company-name { top: 392px; }
  .company-name .wordmark__name { font-size: 38px; }
  .values { top: 462px; left: 38px; width: 240px; text-align: left; list-style: none; }
  .values__item {
    display: flex; align-items: flex-start; gap: 12px;
    color: var(--white); font-size: 21px; line-height: 1.15; margin-bottom: 16px;
  }
  .values__icon { flex: 0 0 16px; width: 16px; height: 16px; margin-top: 5px; }
  .website {
    top: 688px; left: 20px; width: 270px;
    font-family: var(--font-serif); font-size: 12px; color: var(--white);
    transform: rotate(-11deg); transform-origin: left center;
  }

  /* Banner 2 */
  .headline { font-family: var(--font-display); line-height: .92; }
  .headline__white { color: var(--white); }
  .headline__green { color: var(--green); }
  .trader-headline { top: 34px; }
  .trader-headline .headline__white { font-size: 58px; }
  .trader-headline .headline__green { font-size: 72px; }
  .values-inline { top: 410px; color: var(--white); font-weight: 700; font-size: 15px; line-height: 1.55; }
  .program {
    font-family: var(--font-display); font-weight: 400;
    font-size: 28px; line-height: 1.1; white-space: nowrap;
  }
  .program-block__rule { height: 1px; background: var(--white); margin: 0 auto; width: 230px; }
  .trader-program { top: 468px; color: var(--white); }
  .trader-program .program { margin: 3px 0 2px; }
  .contact { font-size: 15px; color: var(--white); line-height: 1.5; }
  .contact__lead strong { font-weight: 700; }
  .contact__email { font-size: 13.5px; }
  .contact__phone { display: flex; align-items: center; justify-content: center; gap: 6px; font-size: 18px; }
  .contact__phone svg { width: 18px; height: 18px; }
  .trader-contact { top: 514px; }
  .trader-wordmark { top: 672px; }
  .trader-wordmark .wordmark__name, .challenge-wordmark .wordmark__name { font-size: 34px; }

  /* Banner 3 */
  .challenge-headline { top: 26px; transform: rotate(-7deg); }
  .challenge-headline .headline__white { font-size: 44px; }
  .challenge-headline .headline__green { font-size: 46px; }
  .challenge-program { top: 494px; }
  .challenge-program .program { color: var(--green); margin-bottom: 4px; }
  .challenge-program .program-block__rule { margin-bottom: 6px; }
  .challenge-wordmark { top: 684px; }
</style>
</head>
<body>
<main class="canvas">

  <!-- Banner 1: company -->
  <section class="banner banner--company" aria-label="Company banner">
    <svg class="banner__shapes" viewBox="0 0 300 740">
      <defs>
        <linearGradient id="officeTone" x1="0" y1="0" x2="1" y2="1">
          <stop offset="0" stop-color="#d9dcdc"/>
          <stop offset=".55" stop-color="#a9adae"/>
          <stop offset="1" stop-color="#5d6264"/>
        </linearGradient>
        <linearGradient id="chartTone" x1="0" y1="0" x2="0" y2="1">
          <stop offset="0" stop-color="#1b1b1b"/>
          <stop offset="1" stop-color="#000000"/>
        </linearGradient>
      </defs>
      <rect x="0" y="240" width="300" height="440" fill="url(#chartTone)" role="img" aria-label="Faint market chart texture behind the company name"/>
      <polygon points="0,0 300,0 300,232 0,196" fill="url(#officeTone)" role="img" aria-label="Photo of the trading office with desks and monitors"/>
      <polygon points="0,196 300,232 300,246 0,268" fill="var(--green)"/>
      <polygon points="0,740 0,706 300,640 300,740" fill="var(--green)"/>
    </svg>

    <div class="layer company-mark"><span class="company-mark__circle"></span></div>
    <div class="layer company-name wordmark"><span class="wordmark__name">MERIDALE</span></div>

    <ul class="layer values">
      <li class="values__item">
        <svg class="values__icon" viewBox="0 0 16 16"><rect x="2" y="2" width="12" height="12" rx="2" fill="var(--green)"/></svg>Challenging
      </li>
      <li class="values__item">
        <svg class="values__icon" viewBox="0 0 16 16"><circle cx="8" cy="6" r="5" fill="none" stroke="var(--green)" stroke-width="2"/><path d="M5 10 L4 16 L8 13 L12 16 L11 10" fill="var(--green)"/></svg>Rewarding
      </li>
      <li class="values__item">
        <svg class="values__icon" viewBox="0 0 16 16"><path d="M1 9 L5 5 L8 7 L11 5 L15 9 L10 13 Z" fill="var(--green)"/></svg>Passionate
      </li>
      <li class="values__item">
        <svg class="values__icon" viewBox="0 0 16 16"><circle cx="8" cy="7" r="5" fill="none" stroke="var(--green)" stroke-width="1.6"/><rect x="6" y="12" width="4" height="3" fill="var(--green)"/></svg>Entrepreneurial<br>Focused
      </li>
    </ul>

    <p class="layer website">www.meridalecapital.com.au</p>
  </section>

  <!-- Banner 2: trader -->
  <section class="banner banner--trader" aria-label="Graduate trader banner">
    <svg class="banner__shapes" viewBox="0 0 300 740">
      <defs>
        <radialGradient id="fairTone" cx=".5" cy=".5" r=".6">
          <stop offset="0" stop-color="#b9763a"/>
          <stop offset=".6" stop-color="#5c6a80"/>
          <stop offset="1" stop-color="#2c3440"/>
        </radialGradient>
      </defs>
      <polygon points="0,245 300,284 300,660 0,596" fill="var(--green)"/>
      <circle cx="145" cy="275" r="106" fill="var(--white)"/>
      <circle cx="145" cy="275" r="100" fill="url(#fairTone)" role="img" aria-label="Overhead photo of students visiting booths at a university careers fair"/>
    </svg>

    <h1 class="layer headline trader-headline">
      <span class="headline__white">WANT TO BE</span><br>
      <span class="headline__green">REWARDED?</span>
    </h1>

    <p class="layer values-inline">Challenging | Rewarding | Passionate<br>| Entrepreneurial Focused</p>

    <div class="layer trader-program">
      <div class="program-block__rule"></div>
      <h2 class="program">GRADUATE TRADER PROGRAM</h2>
      <div class="program-block__rule"></div>
    </div>

    <div class="layer contact trader-contact">
      <p class="contact__lead">Please <strong>CONTACT</strong> us at</p>
      <p class="contact__email">careers@meridalecapital.com.au</p>
      <p class="contact__phone">
        <svg viewBox="0 0 18 18"><circle cx="9" cy="9" r="8" fill="none" stroke="var(--white)" stroke-width="1.4"/><path d="M6 4.5 L7.6 4.5 L8.2 7 L7 7.8 Q8 10 10.2 11 L11 9.8 L13.5 10.4 L13.5 12 Q9 13 6 9 Q5 6.5 6 4.5Z" fill="var(--white)"/></svg>
        (02) 7156 4830
      </p>
    </div>

    <div class="layer trader-wordmark wordmark">
      <span class="wordmark__dot"></span><span class="wordmark__name">MERIDALE</span>
    </div>
  </section>

  <!-- Banner 3: fresh challenges -->
  <section class="banner banner--challenge" aria-label="Fresh challenges banner">
    <svg class="banner__shapes" viewBox="0 0 300 740">
      <defs>
        <linearGradient id="expoTone" x1="0" y1="0" x2="1" y2="1">
          <stop offset="0" stop-color="#6f7d8c"/>
          <stop offset=".5" stop-color="#8a4a4a"/>
          <stop offset="1" stop-color="#3f5f86"/>
        </linearGradient>
      </defs>
      <rect x="0" y="0" width="300" height="740" fill="var(--white)"/>
      <polygon points="0,0 300,0 300,172 0,214" fill="var(--black)"/>
      <polygon points="0,222 300,184 300,192 0,230" fill="var(--green)"/>
      <polygon points="0,230 300,192 300,470 0,440" fill="url(#expoTone)" role="img" aria-label="Photo of a busy careers expo hall with students and stands"/>
      <polygon points="0,440 300,470 300,484 0,454" fill="var(--green)"/>
      <polygon points="0,466 300,492 300,666 0,640" fill="var(--black)"/>
    </svg>

    <h1 class="layer headline challenge-headline">
      <span class="headline__white">WANT TO FACE</span><br>
      <span class="headline__green">FRESH CHALLENGES</span><br>
      <span class="headline__white">EACH DAY?</span>
    </h1>

    <div class="layer challenge-program">
      <h2 class="program">GRADUATE TRADER PROGRAM</h2>
      <div class="program-block__rule"></div>
      <div class="contact">
        <p class="contact__lead">Please <strong>CONTACT</strong> us at</p>
        <p class="contact__email">careers@meridalecapital.com.au</p>
        <p class="contact__phone">
          <svg viewBox="0 0 18 18"><circle cx="9" cy="9" r="8" fill="none" stroke="var(--white)" stroke-width="1.4"/><path d="M6 4.5 L7.6 4.5 L8.2 7 L7 7.8 Q8 10 10.2 11 L11 9.8 L13.5 10.4 L13.5 12 Q9 13 6 9 Q5 6.5 6 4.5Z" fill="var(--white)"/></svg>
          (02) 7156 4830
        </p>
      </div>
    </div>

    <div class="layer challenge-wordmark wordmark">
      <span class="wordmark__dot"></span><span class="wordmark__name">MERIDALE</span>
    </div>
  </section>

</main>
</body>
</html>
```